Stationary and business cards for Meridale Wellness Clinic
Brightwater Meridale Wellness Clinic
Stationary and business cards for Meridale Wellness Clinic - Health
Creative Brief
Use same font as used in my logo
Use whatever fonts you feel works with the logo
Bright & Fun-filled
Dr. Marcus T. Falk
Chiropractic Physician
5182 Orvalle Park Rd. Ste. B Sarasota, FL 34871
wellpath7crew@mailnest.example
www.falkspinecare.example
when they go to the website, they need to click on other services in the top right of the page, and go to: functional endocrine, to read about what I do . I'm not sure how we can direct them to do that on a business card. Also, this is a separate business located within Falk Chiropractic Center,and has nothing to do with Chiropractic Care...... Use whatever fonts you feel works with the logo, or the same as the logo
Lack of energy, sleep problems, weight gain, and body pains are not normal processes of aging...You don't have to live with it! Call us today to reserve a seat at our next free seminar to learn how we can help you!

```html
<!DOCTYPE html>
<html lang="en">
<head>
<meta charset="utf-8">
<title>Brightwater Meridale Wellness Clinic – Business Card</title>
<link href="https://fonts.googleapis.com/css2?family=Cinzel:wght@600&family=Crimson+Text:ital,wght@0,400;0,600;1,600&display=swap" rel="stylesheet">
<style>
  :root {
    --stage: #1d1d1f;
    --card: #ffffff;
    --card-soft: #f1f2f2;
    --green: #5a9a2a;
    --green-light: #cfe3b8;
    --orange-start: #f7b51c;
    --orange-mid: #f07a1f;
    --orange-end: #d9361f;
    --ink: #4a4a4a;
    --white: #ffffff;
  }
  * { margin: 0; padding: 0; box-sizing: border-box; }
  html, body { width: 1200px; height: 871px; overflow: hidden; background: var(--stage); }
  .stage { position: relative; width: 1200px; height: 871px; }
  .card {
    position: absolute; left: 250px; width: 700px; height: 400px;
    background: linear-gradient(160deg, var(--card) 0%, var(--card-soft) 100%);
    border-radius: 14px; overflow: hidden;
  }
  .card--back { top: 20px; }
  .card--front { top: 451px; }

  /* Back */
  .intro-list { position: absolute; left: 60px; top: 120px; list-style: none;
    font-family: "Crimson Text", serif; font-size: 24px; color: var(--ink); line-height: 1.6; }
  .intro-list li { display: flex; align-items: center; gap: 14px; }
  .intro-list li::before { content: ""; width: 11px; height: 11px; border: 2px solid var(--green); border-radius: 50%; }
  .intro-note { position: absolute; right: 50px; top: 110px; width: 300px;
    font-family: "Crimson Text", serif; font-size: 19px; color: var(--ink); line-height: 1.45; text-align: right; }
  .intro-note strong { color: var(--orange-mid); font-weight: 600; }

  /* Front */
  .brand { position: absolute; left: 250px; top: 46px; display: flex; align-items: center; gap: 14px; }
  .brand-dot { width: 48px; height: 48px; border-radius: 50%; background: var(--green); flex: none; }
  .brand-name { font-family: "Cinzel", serif; font-weight: 600; color: var(--green); font-size: 44px; letter-spacing: 1px; line-height: 1; }
  .brand-sub { position: absolute; left: 312px; top: 104px; font-family: "Cinzel", serif; font-weight: 600;
    color: var(--green); font-size: 19px; letter-spacing: 2px; }
  .contact-band { position: absolute; left: 0; bottom: 0; width: 100%; height: 205px;
    background: linear-gradient(90deg, var(--orange-start) 0%, var(--orange-mid) 45%, var(--orange-end) 100%); }
  .emblem-space { position: absolute; left: 38px; top: 120px; }
  .person { position: absolute; left: 220px; top: 38px; color: var(--white); font-family: "Crimson Text", serif; }
  .person-name { font-style: italic; font-weight: 600; font-size: 22px; }
  .person-role, .person-address { font-size: 16px; line-height: 1.35; }
  .person-role { margin-bottom: 14px; }
  .lines { position: absolute; left: 450px; top: 38px; color: var(--white); font-family: "Crimson Text", serif; font-size: 16px; line-height: 1.35; }
  .website { position: absolute; left: 450px; bottom: 22px; color: var(--white); font-family: "Crimson Text", serif; font-size: 17px; }
</style>
</head>
<body>
<div class="stage">
  <section class="card card--back">
    <ul class="intro-list">
      <li>Lack of energy,</li>
      <li>sleep problems,</li>
      <li>weight gain,</li>
      <li>body pains...</li>
    </ul>
    <p class="intro-note">...are not normal processes of aging. You don't have to live with it! <strong>Call us today</strong> to reserve a seat at our next free seminar to learn how we can help you!</p>
  </section>

  <section class="card card--front">
    <div class="brand">
      <span class="brand-dot"></span>
      <span class="brand-name">BRIGHTWATER</span>
    </div>
    <div class="brand-sub">MERIDALE WELLNESS CLINIC</div>

    <div class="contact-band">
      <div class="person">
        <p class="person-name">Dr. Marcus T. Falk</p>
        <p class="person-role">Chiropractic Physician</p>
        <p class="person-address">5182 Orvalle Park Rd. Ste. B<br>Sarasota, FL 34871</p>
      </div>
      <div class="lines">
        <p>P: 941.555.0137</p>
        <p>F: 941.555.0138</p>
        <p>E: wellpath7crew@mailnest.example</p>
      </div>
      <p class="website">www.falkspinecare.example</p>
    </div>

    <svg class="emblem-space" width="160" height="160" viewBox="0 0 160 160" role="img" aria-label="Clinic emblem area">
      <circle cx="80" cy="80" r="76" fill="var(--green-light)"/>
    </svg>
  </section>
</div>
</body>
</html>
```